Business card for Chiropractic clinics needs reworked / redesigned

The business card in attachment was designed 10 years ago. It is in need of an update.
We have 2 clinics:
HALSPUNT VORDA & HALSPUNT MIRBE
Only one address needs to be on the card for doctors that only work in one clinic and two addresses need to be on the card for the doctors that work in both clinics.

Target Market(s)

patients/referrers

Industry/Entity Type

Medical

Contact Information for Business Card

Logo (in full or zoomed-in)
Clinic Name
Doctor name and title
clinic address, website, tel, email

Font styles to use
Sans Serif

Colors

Designer to choose colors to be used in the design.

Requirements
Must have
• Good contrast/readability
• We like modern minimalistic designs
• The Bcard needs to project our very high standard of proficiency/professionalism
Should not have
• Not curly
• Not to much colours

```html
<!DOCTYPE html>
<html lang="en">
<head>
<meta charset="utf-8">
<title>Halspunt business card</title>
<link href="https://fonts.googleapis.com/css2?family=Lato:wght@400;700;900&display=swap" rel="stylesheet">
<style>
  :root {
    --bg: #1d1e20;
    --green: #5cff2e;
    --green-dark: #3fd81a;
    --ink: #1a1a1a;
    --paper: #ffffff;
    --rule: #4aa89a;
  }
  * { box-sizing: border-box; margin: 0; padding: 0; }
  html, body { width: 1200px; height: 1200px; overflow: hidden; background: var(--bg); }
  body { font-family: "Lato", sans-serif; position: relative; }

  .card {
    position: absolute;
    left: 200px;
    width: 800px;
    height: 516px;
    overflow: hidden;
  }
  .card--front { top: 60px; background: var(--green); }
  .card--back { top: 624px; background: var(--paper); }

  /* front */
  .front-brand {
    position: absolute;
    right: 90px;
    top: 210px;
    color: var(--paper);
    font-weight: 400;
    font-size: 44px;
    letter-spacing: 1px;
    text-align: right;
    line-height: 1.15;
  }
  .front-brand__mark {
    position: absolute;
    left: 90px;
    top: 190px;
    width: 136px;
    height: 136px;
    border-radius: 50%;
    border: 8px solid var(--paper);
  }

  /* back */
  .back-band {
    position: absolute;
    left: 0; right: 0; bottom: 0;
    height: 84px;
    background: var(--green);
  }
  .back-mark {
    position: absolute;
    left: 60px;
    top: 150px;
    width: 150px;
    height: 150px;
    border-radius: 50%;
    background: #d6ffc8;
  }
  .mobile {
    position: absolute;
    right: 48px;
    top: 40px;
    font-size: 16px;
    color: var(--ink);
    display: flex;
    align-items: center;
    gap: 6px;
  }
  .mobile-rule {
    position: absolute;
    right: 0;
    top: 72px;
    width: 300px;
    height: 1px;
    background: var(--rule);
  }
  .doctor {
    position: absolute;
    left: 260px;
    top: 120px;
  }
  .doctor__name {
    color: var(--green-dark);
    font-weight: 700;
    font-size: 30px;
  }
  .doctor__name strong { font-weight: 900; }
  .doctor__role {
    color: var(--ink);
    font-size: 16px;
    letter-spacing: .5px;
    margin-top: 4px;
    margin-left: 120px;
  }
  .clinic {
    position: absolute;
    top: 250px;
    color: var(--ink);
    font-size: 18px;
    line-height: 1.45;
  }
  .clinic--vorda { left: 260px; }
  .clinic--mirbe { left: 545px; top: 210px; }
  .clinic__title { font-weight: 900; font-size: 18px; letter-spacing: .3px; }
  .clinic__title span { color: var(--green-dark); }
  .clinic__row { display: flex; align-items: center; gap: 8px; }
  .clinic__row svg { flex: none; }
  .divider {
    position: absolute;
    left: 510px;
    top: 215px;
    width: 2px;
    height: 120px;
    background: linear-gradient(var(--paper), #2a6b2a, var(--paper));
  }
</style>
</head>
<body>

<section class="card card--front" aria-label="Card front">
  <div class="front-brand__mark"></div>
  <div class="front-brand">HALSPUNT<br>VORDA &amp; MIRBE</div>
</section>

<section class="card card--back" aria-label="Card back">
  <div class="back-mark"></div>

  <div class="mobile">
    <svg width="10" height="16" viewBox="0 0 10 16"><rect x="1" y="1" width="8" height="14" rx="1.5" fill="none" stroke="#3fd81a" stroke-width="1.5"/></svg>
    0.555.12.34.56
  </div>
  <div class="mobile-rule"></div>

  <div class="doctor">
    <div class="doctor__name">Lucas <strong>VERMEERSCH D.C.</strong></div>
    <div class="doctor__role">CHIROPRACTOR</div>
  </div>

  <div class="clinic clinic--vorda">
    <div class="clinic__title">HALSPUNT <span>VORDA</span></div>
    <div class="clinic__row">
      <svg width="16" height="18" viewBox="0 0 16 18"><path d="M8 1a5 5 0 0 1 5 5c0 4-5 9-5 9S3 10 3 6a5 5 0 0 1 5-5z" fill="none" stroke="#3fd81a" stroke-width="2"/><circle cx="8" cy="6" r="1.8" fill="#3fd81a"/></svg>
      Lindenlaan 148
    </div>
    <div class="clinic__row">
      <svg width="16" height="16" viewBox="0 0 16 16"><rect width="16" height="16" rx="3" fill="#3fd81a"/><path d="M5 4l2 2-1 1.5c.7 1.3 1.5 2.1 2.5 2.5L10 9l2 2-1.5 1.5C7 12 4 9 3.5 5.5z" fill="#fff"/></svg>
      09 555 12 40
    </div>
    <div class="clinic__row">
      <svg width="16" height="16" viewBox="0 0 16 16" fill="none" stroke="#3fd81a" stroke-width="1.3"><circle cx="8" cy="8" r="7"/><ellipse cx="8" cy="8" rx="3" ry="7"/><path d="M1 8h14M2.5 4.5h11M2.5 11.5h11"/></svg>
      halspuntvorda.be
    </div>
  </div>

  <div class="divider"></div>

  <div class="clinic clinic--mirbe">
    <div class="clinic__title">HALSPUNT <span>MIRBE</span></div>
    <div class="clinic__row">
      <svg width="16" height="18" viewBox="0 0 16 18"><path d="M8 1a5 5 0 0 1 5 5c0 4-5 9-5 9S3 10 3 6a5 5 0 0 1 5-5z" fill="none" stroke="#3fd81a" stroke-width="2"/><circle cx="8" cy="6" r="1.8" fill="#3fd81a"/></svg>
      Molenstraat 27
    </div>
    <div class="clinic__row">
      <svg width="16" height="16" viewBox="0 0 16 16"><rect width="16" height="16" rx="3" fill="#3fd81a"/><path d="M5 4l2 2-1 1.5c.7 1.3 1.5 2.1 2.5 2.5L10 9l2 2-1.5 1.5C7 12 4 9 3.5 5.5z" fill="#fff"/></svg>
      09 555 78 21
    </div>
    <div class="clinic__row">
      <svg width="16" height="16" viewBox="0 0 16 16" fill="none" stroke="#3fd81a" stroke-width="1.3"><circle cx="8" cy="8" r="7"/><ellipse cx="8" cy="8" rx="3" ry="7"/><path d="M1 8h14M2.5 4.5h11M2.5 11.5h11"/></svg>
      halspuntmirbe.be
    </div>
  </div>

  <div class="back-band"></div>
</section>

</body>
</html>
```